" Não vendemos nossos serviços "no varejo". Somos chamados a participar de projetos de investimento no Brasil ainda na fase de concepção, sob acordo de confidencialidade, buscando alimentar a modelagem financeira com os inputs tributários que frequentemente são cruciais na definição de viabilidade do projeto. Também somos chamados por nossos clientes para avaliar ou alocar contratualmente riscos decorrentes de contingências fiscais, especialmente em fusões e aquisições de empresas. E, ainda, patrocinar defesas ou pleitos em processos administrativos ou judiciais, sempre tendo como parte adversária o fisco (federal, estadual ou municipal). Atuamos em um ambiente profissional onde ética, compliance, qualidade e comprometimento são premissas. O propósito de nossa empresa é a criação de valor de modo sustentável, em questões fiscais, para negócios empreendidos no Brasil. "

```html
<!DOCTYPE html>
<html lang="pt-BR">
<head>
<meta charset="utf-8">
<title>LAC — Pasta institucional</title>
<link href="https://fonts.googleapis.com/css2?family=Montserrat:wght@400;500;600&display=swap" rel="stylesheet">
<style>
  :root {
    --bg: #e4e6ea;
    --paper: #ffffff;
    --navy: #1f2a5c;
    --blue: #5f7fb8;
    --blue-light: #a9bcdc;
    --ghost: #e3e5ea;
    --text: #5a6270;
  }
  * { box-sizing: border-box; margin: 0; padding: 0; }
  html, body { width: 1200px; height: 1200px; overflow: hidden; }
  body {
    background: var(--bg);
    font-family: "Montserrat", sans-serif;
    display: flex; align-items: center; justify-content: center;
  }
  .folder { display: flex; box-shadow: 0 10px 30px rgba(0,0,0,.12); }
  .panel {
    position: relative; width: 520px; height: 740px;
    background: var(--paper); overflow: hidden;
  }
  .panel--back { border-right: 1px solid #eef0f3; }
  .panel__band {
    position: absolute; left: 0; right: 0; bottom: 0; height: 14px;
    background: linear-gradient(to bottom, var(--blue-light), var(--blue));
  }
  .panel__rule {
    position: absolute; left: 0; right: 0; bottom: 14px; height: 3px;
    background: var(--blue-light); opacity: .6;
  }
  .signature {
    position: absolute; top: 46px; left: 70px;
    display: flex; align-items: flex-start; gap: 10px;
  }
  .signature__names {
    list-style: none; font-size: 7px; font-weight: 500; letter-spacing: .8px;
    color: var(--blue); line-height: 1.45; text-transform: uppercase;
  }
  .signature__name { font-size: 14px; font-weight: 600; color: var(--navy); letter-spacing: 1px; }
  .ghost-name {
    position: absolute; top: 230px; left: 60px;
    font-size: 150px; font-weight: 500; color: var(--ghost); letter-spacing: 6px;
    line-height: 1;
  }
  .contact {
    position: absolute; left: 30px; bottom: 32px;
    font-size: 7px; color: var(--text); line-height: 1.9;
  }
  .contact__item { display: flex; align-items: center; gap: 5px; }
  .contact__item svg { width: 8px; height: 8px; fill: var(--blue); }
  .cover-name {
    position: absolute; top: 50%; left: 50%; transform: translate(-50%, -80%);
    font-size: 64px; font-weight: 500; color: var(--navy); letter-spacing: 4px;
  }
</style>
</head>
<body>
  <main class="folder">
    <section class="panel panel--back">
      <div class="signature">
        <ul class="signature__names">
          <li>Lemos</li><li>Arantes</li><li>Cunha</li><li>Tributário</li>
        </ul>
        <span class="signature__name">LAC</span>
      </div>
      <div class="ghost-name" aria-hidden="true">LAC</div>
      <address class="contact">
        <p class="contact__item">
          <svg viewBox="0 0 10 10"><circle cx="5" cy="5" r="5"/></svg>
          Rua das Acácias 120, 5º andar · Centro · Porto Alegre · RS · CEP 90010-000
        </p>
        <p class="contact__item">
          <svg viewBox="0 0 10 10"><circle cx="5" cy="5" r="5"/></svg>
          contato@lemosarantes.com.br
        </p>
        <p class="contact__item">
          <svg viewBox="0 0 10 10"><circle cx="5" cy="5" r="5"/></svg>
          (51) 3200-4100
        </p>
      </address>
      <div class="panel__rule"></div>
      <div class="panel__band"></div>
    </section>
    <section class="panel panel--front">
      <h1 class="cover-name">LAC</h1>
      <div class="panel__rule"></div>
      <div class="panel__band"></div>
    </section>
  </main>
</body>
</html>
```